Valdoro Global Journeys Facebook Page

I would like to have a very professional and unique Facebook page for my business
www.valdoroglobaljourneys.com

```html
<!DOCTYPE html>
<html lang="en">
<head>
<meta charset="utf-8">
<title>Valdoro Global Journeys – Facebook Cover</title>
<link href="https://fonts.googleapis.com/css2?family=Open+Sans:ital,wght@0,700;1,300;1,800&display=swap" rel="stylesheet">
<style>
  :root {
    --page-bg: #e8e8e8;
    --teal: #1293a8;
    --teal-deep: #1d7c7e;
    --night: #232526;
    --white: #ffffff;
  }
  html, body {
    margin: 0;
    width: 1200px;
    height: 1155px;
    overflow: hidden;
    background: var(--page-bg);
  }
  .cover {
    position: absolute;
    left: 40px;
    top: 370px;
    width: 1120px;
    height: 414px;
    display: block;
  }
  .headline { font-family: "Open Sans", Arial, sans-serif; fill: var(--white); text-anchor: middle; font-style: italic; }
  .headline .light { font-weight: 300; }
  .headline .heavy { font-weight: 800; }
  .brand-name { font-family: "Open Sans", Arial, sans-serif; font-weight: 700; fill: var(--white); font-size: 14px; letter-spacing: 0.5px; }
</style>
</head>
<body>
<svg class="cover" viewBox="0 0 1108 410" xmlns="http://www.w3.org/2000/svg" aria-label="Valdoro Global Journeys cover: Visit the top of the world, challenge yourself">
  <defs>
    <linearGradient id="peakLeft" x1="0" y1="0" x2="0" y2="1">
      <stop offset="0" stop-color="#3f79c0"/>
      <stop offset="0.35" stop-color="#c9d6e6"/>
      <stop offset="0.6" stop-color="#7f8ea0"/>
      <stop offset="1" stop-color="#8a5528"/>
    </linearGradient>
    <linearGradient id="templeCenter" x1="0" y1="0" x2="0" y2="1">
      <stop offset="0" stop-color="#3a3b36"/>
      <stop offset="1" stop-color="#1c1c1d"/>
    </linearGradient>
    <linearGradient id="peakRight" x1="0" y1="0" x2="0" y2="1">
      <stop offset="0" stop-color="#2f6fc4"/>
      <stop offset="0.45" stop-color="#dfe6ee"/>
      <stop offset="1" stop-color="#6c6f6e"/>
    </linearGradient>
  </defs>

  <rect class="cover-base" width="1108" height="410" fill="var(--teal)"/>

  <polygon class="photo photo-left" role="img" aria-label="Photo: snow-capped Himalayan peak above a brown valley" points="80,0 440,0 305,410 0,410 0,215" fill="url(#peakLeft)"/>

  <polygon class="photo photo-center" role="img" aria-label="Photo: monastery with prayer flags at dusk" points="462,0 795,0 665,410 325,410" fill="url(#templeCenter)"/>

  <polygon class="photo photo-right" role="img" aria-label="Photo: trekkers on rocks below Everest" points="812,0 1060,0 1108,0 1108,175 1045,340 870,340 870,410 682,410" fill="url(#peakRight)"/>
  <polygon class="corner-accent" points="1108,175 1108,340 1045,340" fill="var(--teal)"/>

  <g class="headline">
    <text class="light" x="578" y="72" font-size="34">VISIT THE</text>
    <text class="heavy" x="578" y="165" font-size="92">TOP</text>
    <text class="light" x="532" y="213" font-size="44">OF THE</text>
    <text class="heavy" x="535" y="268" font-size="50">WORLD</text>
    <text class="light" x="515" y="314" font-size="36">CHALLENGE</text>
    <text class="heavy" x="527" y="367" font-size="46">YOURSELF</text>
  </g>

  <g class="brand-block">
    <rect x="870" y="340" width="238" height="70" fill="var(--teal-deep)"/>
    <circle cx="940" cy="375" r="20" fill="none" stroke="var(--white)" stroke-width="2.5"/>
    <text class="brand-name" x="968" y="371">VALDORO</text>
    <text class="brand-name" x="968" y="389">GLOBAL JOURNEYS</text>
  </g>
</svg>
</body>
</html>
```